Auto and Home Insurance Quote Letter

I am an insurance agent and i have been mailing out a front back auto and home insurance quotes in black and white to prospects in my area. I would like the letter to be updated with a new look and some new graphics that would help catch the attention of the prospects I am mailing to. Anything that would help the prospect to call my office.

```html
<!DOCTYPE html>
<html lang="en">
<head>
<meta charset="utf-8">
<title>Harbor Lane Insurance Agency – Home Insurance Quote</title>
<link href="https://fonts.googleapis.com/css2?family=Montserrat:wght@400;500;600;700;800&display=swap" rel="stylesheet">
<style>
:root{
  --band:#237d9c;
  --navy:#14385a;
  --sky:#bde0ef;
  --teal:#85c1cc;
  --rule:#8cc4e0;
  --ink:#1a1a1a;
  --orange:#f29a1e;
  --red:#d8474d;
  --red-dark:#8e2a30;
  --white:#ffffff;
}
*{margin:0;padding:0;box-sizing:border-box}
html,body{width:1200px;height:900px;overflow:hidden;background:var(--white)}
body{font-family:"Montserrat",sans-serif;color:var(--ink);position:relative}
.letter{position:absolute;left:292px;top:13px;width:622px;height:879px;border-left:1px solid #888;border-right:1px solid #888;background:var(--white)}
.band-top{position:absolute;left:0;top:0;width:100%;height:17px;background:var(--band)}
.rule-top{position:absolute;left:0;top:18.5px;width:100%;height:2px;background:var(--band)}
.brand{position:absolute;left:0;top:60px;width:100%;text-align:center;color:var(--navy)}
.brand-name{display:inline-flex;align-items:center;gap:8px;font-size:17px;font-weight:600;letter-spacing:.3px;line-height:1}
.brand-mark{width:12px;height:12px;background:var(--navy)}
.brand-tag{margin-top:9px;font-size:7.5px;letter-spacing:2.4px;color:#333}
.pitch{position:absolute;left:36px;top:158px;width:549px;height:91px;display:flex}
.pitch-lead{width:275px;background:var(--sky);padding:12px 15px;font-size:12.5px;line-height:15px;color:var(--navy);text-align:justify}
.pitch-call{flex:1;background:var(--teal);padding:12px 15px;font-size:12.5px;line-height:15px;color:var(--navy);position:relative}
.pitch-call::before{content:"";position:absolute;left:0;top:65px;border-top:6px solid transparent;border-bottom:6px solid transparent;border-left:8px solid var(--sky)}
.pitch b{font-weight:700}
.example{position:absolute;left:36px;top:265px;width:549px;height:32px;border:2px dashed var(--band);border-radius:2px;text-align:center;font-size:12.3px;font-weight:700;line-height:28px;color:var(--ink)}
.home-facts{position:absolute;left:36px;top:321px;width:549px;height:28px;background:var(--teal);text-align:center;font-size:11.6px;font-weight:600;line-height:28px;color:var(--ink)}
.home-facts span{margin:0 9px}
.coverage{position:absolute;left:36px;top:365px;width:549px;height:168px;border:1.5px solid var(--rule)}
.coverage-head{height:23px;background:var(--sky);border-bottom:1.5px solid var(--rule);padding-left:4px;font-size:12.3px;font-weight:600;line-height:22px}
.coverage-list{position:absolute;left:17px;top:36px;font-size:11.5px;line-height:13.8px}
.coverage-list li{list-style:none;display:flex}
.coverage-list .label{width:189px}
.premium{position:absolute;left:320px;top:50px;text-align:center;color:var(--orange);font-weight:700}
.premium-title{font-size:15.5px;text-shadow:1px 1px 0 #fde6b8,-1px -1px 0 #fde6b8}
.premium-amount{font-size:40px;font-weight:800;margin-top:6px;text-shadow:2px 2px 0 #fde6b8,-1px -1px 0 #fde6b8,3px 3px 4px rgba(0,0,0,.25)}
.disclaimer{position:absolute;left:37px;top:539px;font-size:9px;line-height:11.5px}
.signoff{position:absolute;left:36px;top:638px;font-size:11.5px}
.signature{position:absolute;left:38px;top:670px;width:136px;height:36px;background:linear-gradient(90deg,#e6e6e6,#f3f3f3);border-radius:3px}
.signer{position:absolute;left:37px;top:722px;font-size:11.5px;line-height:14px}
.roof-offer{position:absolute;left:324px;top:636px;width:220px;height:128px}
.roof-offer svg{position:absolute;inset:0}
.roof-text{position:absolute;left:0;top:7px;width:100%;text-align:center;color:var(--white);font-size:10.6px;line-height:13.7px}
.roof-text strong{display:block;font-size:13.4px;font-weight:700;line-height:16.5px}
.roof-text .cta{margin-top:1px}
.rule-bottom{position:absolute;left:0;top:830px;width:100%;height:5px;background:var(--band)}
.band-bottom{position:absolute;left:0;top:840px;width:100%;height:39px;background:var(--band);color:var(--white);text-align:center;font-size:15px;font-weight:600;line-height:37px}
</style>
</head>
<body>
<main class="letter">
  <div class="band-top"></div>
  <div class="rule-top"></div>

  <header class="brand">
    <div class="brand-name"><span class="brand-mark"></span>HARBOR LANE INSURANCE AGENCY</div>
    <div class="brand-tag">AUTO · HOME · LIFE · BUSINESS</div>
  </header>

  <section class="pitch">
    <p class="pitch-lead">If you are tired of paying too much for Home Insurance and <b>want all your insurance needs handled under one agency</b></p>
    <p class="pitch-call">Then call us at <b>407-555-0182</b>.<br>One call is all it takes to see if you’ve got the right coverage at the right price.</p>
  </section>

  <div class="example">BELOW IS AN EXAMPLE OF A RECENT HOME INSURANCE POLICY IN ORLANDO</div>

  <div class="home-facts">Year Built: 2015<span>•</span>4 Bedrooms<span>•</span>Heated Square Feet: 2568</div>

  <section class="coverage">
    <div class="coverage-head">Coverage Limit</div>
    <ul class="coverage-list">
      <li><span class="label">A - Dwelling Protection</span><span>$305,000.00</span></li>
      <li><span class="label">B - Other Structures</span><span>6,100.00</span></li>
      <li><span class="label">C – Personal Property</span><span>106,750.00</span></li>
      <li><span class="label">D – Loss of Use</span><span>30,500.00</span></li>
      <li><span class="label">E - Personal Liability</span><span>$300,000</span></li>
      <li><span class="label">F - Medical Protection</span><span>$1,000.00</span></li>
      <li><span class="label">AOP Deductible</span><span>$2,500</span></li>
      <li><span class="label">Hurricane&nbsp; Deductible</span><span>2%</span></li>
    </ul>
    <div class="premium">
      <div class="premium-title">Total Annual Premium</div>
      <div class="premium-amount">$725.00</div>
    </div>
  </section>

  <p class="disclaimer">The quoted premium is a sample premium based on a recent policy purchased in Orlando.<br>Premium will differ based on information obtained on your application.</p>

  <p class="signoff">Sincerely,</p>
  <div class="signature" role="img" aria-label="Handwritten signature of the agency principal"></div>
  <p class="signer">Daniel Harbor<br>Agency Principal</p>

  <aside class="roof-offer">
    <svg viewBox="0 0 220 128" aria-hidden="true">
      <path d="M8 3 L212 0 Q219 1 218 9 L196 120 Q194 127 186 127 L28 121 Q21 121 19 114 L1 11 Q1 4 8 3 Z" fill="var(--red)" stroke="var(--red-dark)" stroke-width="3" stroke-linejoin="round"/>
    </svg>
    <div class="roof-text">
      <strong>Newer Roof,<br>Save Even More.</strong>
      If you have a newer roof,<br>you may qualify for added<br>savings your Keystone<br>home owners insurance.
      <strong class="cta">Ask me today</strong>
    </div>
  </aside>

  <div class="rule-bottom"></div>
  <footer class="band-bottom">407-555-0182 • Orlando, FL • HarborLaneAgency.com</footer>
</main>
</body>
</html>
```